Industrial Professional Business Card Design (Vantrel Systems)

Would like professional looking business cards. Not too busy leaning towards minimal. Should have a slogan like:
"Industrial Automation and Control".

We are a tech company that programs industrial PLC computers. We also develop custom hardware solutions. Please use the logo for inspiration.

Target Market(s)

Mining, industrial, processing, automation, factory

Industry/Entity Type

Engineering

Contact Information for Business Card

Name, phone, email, website. job title.

Font styles to use
Other font styles liked:
• droid sans

Requirements
Must have
• Use colours that go well with the logo. Not too busy design.

```html
<!DOCTYPE html>
<html lang="en">
<head>
<meta charset="utf-8">
<title>Vantrel Systems — Business Card</title>
<link rel="stylesheet" href="https://fonts.googleapis.com/css2?family=Open+Sans:wght@400;600;700&display=swap">
<style>
  :root {
    --backdrop: #3a3b3a;
    --card: #151617;
    --card-edge: #222426;
    --blue: #3d76a3;
    --steel: #8fa2b8;
    --orange: #ec7a3c;
    --divider: #6d7078;
  }
  * { box-sizing: border-box; margin: 0; padding: 0; }
  html, body {
    width: 1200px; height: 825px; overflow: hidden;
    background: var(--backdrop);
    font-family: "Open Sans", sans-serif;
  }
  .stage {
    position: relative; width: 1200px; height: 825px;
    display: flex; align-items: center; justify-content: center; gap: 60px;
  }
  .card {
    position: relative; width: 520px; height: 300px;
    background: var(--card);
    border: 1px solid var(--card-edge);
    border-radius: 4px;
    box-shadow: 0 10px 30px rgba(0,0,0,0.45);
    overflow: hidden;
  }
  /* Front */
  .front-mark {
    position: absolute; left: -40px; top: -60px;
    width: 280px; height: 280px; border-radius: 50%;
    background: var(--blue);
  }
  .front-name {
    position: absolute; right: 34px; bottom: 36px;
    font-size: 34px; font-weight: 400; color: var(--blue);
    letter-spacing: 0.5px;
  }
  /* Back */
  .brand {
    position: absolute; left: 0; top: 0; width: 270px; height: 100%;
    display: flex; flex-direction: column; align-items: center; justify-content: center; gap: 14px;
  }
  .brand-dot { width: 46px; height: 46px; border-radius: 50%; background: var(--orange); }
  .brand-name { font-size: 24px; font-weight: 400; color: var(--blue); }
  .divider {
    position: absolute; left: 270px; top: 70px; width: 1px; height: 160px;
    background: var(--divider);
  }
  .details { position: absolute; left: 300px; top: 78px; }
  .person-name { font-size: 24px; font-weight: 400; color: var(--steel); letter-spacing: 1px; }
  .job-title {
    font-size: 12px; font-weight: 700; color: var(--orange);
    letter-spacing: 2px; margin-top: 2px;
  }
  .contacts { list-style: none; margin-top: 20px; }
  .contacts li {
    display: flex; align-items: center; gap: 10px;
    font-size: 13px; color: var(--blue); line-height: 24px;
  }
  .contacts svg { width: 12px; height: 12px; fill: var(--orange); flex: none; }
</style>
</head>
<body>
<main class="stage">
  <section class="card card-front">
    <div class="front-mark" aria-hidden="true"></div>
    <p class="front-name">Vantrel Systems</p>
  </section>

  <section class="card card-back">
    <div class="brand">
      <div class="brand-dot" aria-hidden="true"></div>
      <p class="brand-name">Vantrel Systems</p>
    </div>
    <div class="divider"></div>
    <div class="details">
      <p class="person-name">Your Name</p>
      <p class="job-title">JOB TITLE</p>
      <ul class="contacts">
        <li>
          <svg viewBox="0 0 24 24" aria-hidden="true"><path d="M6.6 10.8a15 15 0 0 0 6.6 6.6l2.2-2.2c.3-.3.7-.4 1-.2 1.1.4 2.3.6 3.6.6.6 0 1 .4 1 1V20c0 .6-.4 1-1 1A17 17 0 0 1 3 4c0-.6.4-1 1-1h3.5c.6 0 1 .4 1 1 0 1.3.2 2.5.6 3.6.1.3 0 .7-.2 1z"/></svg>
          000.000.0000
        </li>
        <li>
          <svg viewBox="0 0 24 24" aria-hidden="true"><path d="M2 5h20v14H2z M2 5l10 8 10-8" /></svg>
          yourname@vantrel.com
        </li>
        <li>
          <svg viewBox="0 0 24 24" aria-hidden="true"><circle cx="12" cy="12" r="10"/></svg>
          www.vantrel.com
        </li>
      </ul>
    </div>
  </section>
</main>
</body>
</html>
```